Business Card Design needed for logo design project

Our company needs a Business Card Design. Please refer to our original project in the link above.

Industry/Entity Type

Business

```html
<!DOCTYPE html>
<html lang="en">
<head>
<meta charset="utf-8">
<title>Morvane Coastal — Business Card</title>
<link rel="stylesheet" href="https://fonts.googleapis.com/css2?family=Arimo:wght@400;700&display=swap">
<style>
  :root {
    --canvas: #e9e9ea;
    --charcoal: #262627;
    --charcoal-deep: #1e1e1f;
    --stone: #c9c7c5;
    --ink: #232323;
    --sky: #4a8fd4;
    --paper: #f4f4f4;
  }
  * { box-sizing: border-box; margin: 0; padding: 0; }
  html, body {
    width: 1022px;
    height: 1200px;
    overflow: hidden;
    background: var(--canvas);
    font-family: "Arimo", Arial, sans-serif;
  }
  .sheet {
    width: 1022px;
    height: 1200px;
    display: flex;
    flex-direction: column;
    align-items: center;
    justify-content: center;
    gap: 80px;
  }
  .card {
    position: relative;
    width: 860px;
    height: 491px;
    background: var(--charcoal);
    overflow: hidden;
    box-shadow: 0 10px 28px rgba(0, 0, 0, 0.22);
  }
  .card-front__band {
    position: absolute;
    inset: 0;
    width: 100%;
    height: 100%;
  }
  .card-front__brand {
    position: absolute;
    left: 0;
    right: 0;
    top: 200px;
    display: flex;
    flex-direction: column;
    align-items: center;
    gap: 10px;
  }
  .brand-name {
    font-weight: 700;
    letter-spacing: 0.04em;
    text-transform: uppercase;
    line-height: 1;
  }
  .card-front .brand-name {
    font-size: 44px;
    color: var(--ink);
  }
  .brand-tagline {
    font-weight: 700;
    font-size: 15px;
    color: var(--ink);
    letter-spacing: 0.01em;
  }
  .card-back .brand {
    position: absolute;
    left: 60px;
    top: 58px;
    display: flex;
    flex-direction: column;
    gap: 6px;
  }
  .card-back .brand-name {
    font-size: 28px;
    color: var(--paper);
  }
  .card-back .brand-tagline {
    font-weight: 400;
    font-size: 11px;
    color: var(--paper);
  }
  .contact {
    position: absolute;
    left: 60px;
    bottom: 70px;
    color: var(--paper);
  }
  .contact__name {
    font-size: 34px;
    font-weight: 400;
    color: var(--sky);
    margin-bottom: 22px;
  }
  .contact__line {
    font-size: 25px;
    line-height: 1.32;
  }
</style>
</head>
<body>
<main class="sheet">

  <section class="card card-front" aria-label="Business card front">
    <svg class="card-front__band" viewBox="0 0 860 491" preserveAspectRatio="none" aria-hidden="true">
      <path d="M0 70 Q430 20 860 70 L860 380 Q430 430 0 380 Z" fill="var(--stone)"/>
    </svg>
    <div class="card-front__brand">
      <span class="brand-name">Morvane Coastal</span>
      <span class="brand-tagline">Your Trusted Real Estate Advisors</span>
    </div>
  </section>

  <section class="card card-back" aria-label="Business card back">
    <div class="brand">
      <span class="brand-name">Morvane Coastal</span>
      <span class="brand-tagline">Your Trusted Real Estate Advisors</span>
    </div>
    <div class="contact">
      <p class="contact__name">Idris Calder</p>
      <p class="contact__line">555-018-274</p>
      <p class="contact__line">idris@morvanecoastal.com</p>
      <p class="contact__line">morvanecoastal.com</p>
    </div>
  </section>

</main>
</body>
</html>
```